Brenwick Holdings Limited
BrenHold
I agree with jonwel. The logo's resolution is too low. Please provide an Adobe Illustrator File or a larger logo. Thanks.
#7 obviously doesn't get the fact that this is a business card, not a logo. :-)
H! GT please provide eps or ai files for the logo, the png file is too small and not a transparent.. Thanks!

```html
<!DOCTYPE html>
<html lang="en">
<head>
<meta charset="utf-8">
<title>BrenHold business card</title>
<link rel="stylesheet" href="https://fonts.googleapis.com/css2?family=Open+Sans:ital,wght@0,400;0,600;0,700;1,400&display=swap">
<style>
  :root {
    --backdrop: #4a1414;
    --card: #ffffff;
    --ink-grey: #6d6e71;
    --brand-grey: #8a8c8f;
    --brand-blue: #1e6fb8;
    --band-orange: #f26a21;
    --band-green: #4cc21c;
    --band-cyan: #1aa6d8;
    --band-blue: #123f9c;
    --white: #ffffff;
  }
  * { margin: 0; padding: 0; box-sizing: border-box; }
  html, body {
    width: 1200px; height: 931px; overflow: hidden;
    background: var(--backdrop);
    font-family: "Open Sans", Arial, sans-serif;
  }
  .business-card {
    position: absolute; left: 244px; top: 211px;
    width: 663px; height: 384px;
    background: var(--card);
    box-shadow: 0 4px 14px rgba(0,0,0,0.35);
  }
  .brand {
    position: absolute; left: 40px; top: 98px;
    display: flex; align-items: center; gap: 12px;
  }
  .brand-mark { width: 22px; height: 22px; background: var(--brand-blue); }
  .brand-name {
    font-size: 44px; font-weight: 400; color: var(--brand-grey);
    letter-spacing: 1px; line-height: 1;
  }
  .tagline {
    position: absolute; left: 102px; top: 146px;
    font-size: 12px; font-weight: 600; color: var(--brand-blue);
  }
  .holder { position: absolute; left: 105px; top: 252px; }
  .holder-name {
    font-size: 15px; font-weight: 700; color: var(--brand-blue);
    text-transform: uppercase; letter-spacing: 0.3px; line-height: 20px;
  }
  .holder-role { font-size: 14px; font-style: italic; color: var(--ink-grey); line-height: 20px; }
  .address {
    position: absolute; left: 419px; top: 116px;
    font-size: 14px; line-height: 23px; color: var(--ink-grey); font-style: normal;
  }
  .contacts {
    position: absolute; left: 419px; top: 245px;
    list-style: none; font-size: 14px; line-height: 22px; color: var(--ink-grey);
  }
  .contacts b { color: var(--brand-blue); font-weight: 700; }
  .colour-band {
    position: absolute; left: 0; bottom: 0; width: 100%; height: 28px;
    background: linear-gradient(90deg, var(--band-orange) 0%, var(--band-green) 38%, var(--band-cyan) 62%, var(--band-blue) 88%);
  }
  .website {
    position: absolute; left: 421px; top: 4px;
    font-size: 14px; line-height: 20px; font-weight: 700; color: var(--white);
  }
</style>
</head>
<body>
  <article class="business-card">
    <div class="brand">
      <span class="brand-mark"></span>
      <span class="brand-name">brenhold</span>
    </div>
    <p class="tagline">Investing in Technology</p>

    <div class="holder">
      <p class="holder-name">Tom C Vale</p>
      <p class="holder-role">Chief Executive</p>
    </div>

    <address class="address">
      Kestrel Court<br>
      Marlow Road<br>
      Ashbridge<br>
      Westshire<br>
      AB4 7QN
    </address>

    <ul class="contacts">
      <li><b>P:</b> +44 208 555 0142</li>
      <li><b>C:</b> +44 7700 900318</li>
      <li><b>F:</b> +44 208 555 0199</li>
      <li><b>E:</b> tom.vale@brenhold.co.uk</li>
    </ul>

    <div class="colour-band">
      <span class="website">www.brenhold.co.uk</span>
    </div>
  </article>
</body>
</html>
```